Plakat-Design für ein großes, geistliches Konzert für Chor, Orchester und Solisten
Morvanta ist eine sehr kreative, zuverlässige und unkomplizierte Designerin und sehr zu empfehlen!
Zielgruppe
Wir sind eine Kantorei einer Kirchengemeinde, die in jedem Jahr ein großes Konzert für Chor, Orchester und Solisten veranstaltet. In diesem Jahr ist das Konzert in doppeltem Sinn etwas Besonderes. Zum einen weil wir das Konzert in Kooperation mit einer anderen Kantorei bestreiten und zum anderen weil die Anzahl der Mitwirkenden so groß ist, dass wir nicht der Kirche sondern das Konzert in die hiesige Stadthalle verlagern. Die Kirchenmusik präsentiert sozusagen sich außerhalb ihrer eigenen Mauern.
Eine Zielgruppe sollen diejenigen sein, die sich durch den besoneren Veranstaltungsort ansprechen lassen, also eher kirchenfremde Menschen. Das Plakat sollte auch das bestehende Stammpublikum nicht abschrecken, sondern einladen.
Es ist ein Folgeauftrag geplant, und zwar ein Programmheft/Textheft für das Konzert mit dem gleichen Design als Grundlage.
Aufgabenstellung
Das Plakat soll im DIN A3 oder A4 Hochformat erstellt werden.
Zwei weitere Logos von Förderern folgen noch.
Außer der Turm sind alle Logos von Förderern.
Der Turm ist sozusagen unser Markenzeichen und ein Wiedererkennungsmerkmal.
Das Konzert steht unter dem Motto: Aus dem Dunkel ins Helle.
Bezüglich der Textgröße sollte dieses Motto nicht größer sein als z.B. der Komponist und das Werk. Vielmehr soll das Motto durch ein grafisches Element eingearbeitet werden. 'Brauneckert' und 'Velmarung' sollen Eye catcher-Worte sein. Velmarung ist der Titel des Konzertes!

```html
<!DOCTYPE html>
<html lang="de">
<head>
<meta charset="utf-8">
<title>Aus dem Dunkel ins Helle – Konzertplakat</title>
<link href="https://fonts.googleapis.com/css2?family=Alegreya:ital,wght@0,700;1,400&family=Alegreya+Sans:wght@400;500&display=swap" rel="stylesheet">
<style>
  :root {
    --page: #f2f2f0;
    --paper: #ffffff;
    --navy: #3d4a86;
    --navy-soft: #aab1d0;
    --ink-light: #ffffff;
    --tower-red: #c0182b;
    --logo-grey: #333333;
  }
  html, body { margin: 0; padding: 0; overflow: hidden; }
  body { width: 1200px; height: 849px; background: var(--page); position: relative; }
  .poster {
    position: absolute; left: 313px; top: 19px; width: 573px; height: 810px;
    background: var(--paper); border: 1px solid #444; box-sizing: border-box;
  }
  .header-art {
    position: absolute; left: 28px; top: 20px; width: 518px; height: 272px;
    background: linear-gradient(180deg, var(--paper) 0%, var(--navy-soft) 55%, var(--navy) 100%);
  }
  .panel {
    position: absolute; left: 28px; top: 292px; width: 518px; height: 428px;
    background: var(--navy); color: var(--ink-light); text-align: center;
  }
  .motto {
    font-family: "Alegreya", serif; font-style: italic; font-weight: 400;
    font-size: 40px; line-height: 44px; margin: 22px 0 0;
  }
  .work {
    font-family: "Alegreya", serif; font-weight: 700; font-size: 12.5px;
    line-height: 18px; margin: 12px 0 0;
  }
  .details {
    font-family: "Alegreya Sans", sans-serif; font-size: 11.5px; line-height: 16.3px;
    display: grid; grid-template-columns: 1fr 1fr; margin-top: 12px;
  }
  .details .cast { text-align: right; padding-right: 6px; border-right: 1px solid var(--ink-light); }
  .details .facts { text-align: left; padding-left: 6px; }
  .details .gap { height: 12px; }
  .more {
    font-family: "Alegreya Sans", sans-serif; font-size: 11.5px; line-height: 17px;
    position: absolute; left: 0; right: 0; bottom: 12px;
  }
  .more .links span { margin: 0 8px; }
  .brand-tower {
    position: absolute; left: 28px; top: 740px; font-family: "Alegreya Sans", sans-serif;
    font-weight: 500; font-size: 14px; color: var(--tower-red); display: flex; align-items: center; gap: 6px;
  }
  .brand-tower .dot { width: 10px; height: 10px; background: var(--tower-red); border-radius: 50%; }
  .sponsors {
    position: absolute; right: 28px; top: 748px; display: flex; gap: 22px;
    font-family: "Alegreya Sans", sans-serif; font-weight: 500; font-size: 11px; color: var(--logo-grey);
  }
</style>
</head>
<body>
  <main class="poster">
    <div class="header-art" role="img" aria-label="Grafik: Übergang von Hell zu Dunkel mit Notenpult, aufgeschlagenem Notenbuch und aufsteigenden Musiknoten"></div>

    <section class="panel">
      <h1 class="motto">Aus dem Dunkel<br>ins Helle</h1>
      <p class="work">Felix Brauneckert-Haldorf:<br>Choralkantate „Wer still dem Morgen sich vertraut“<br>Velmarung-Sinfonie op. 52</p>
      <div class="details">
        <div class="cast">
          Lena Korvath, Sopran<br>
          Marie-Luise Brandt, Sopran<br>
          Jonas Elverum, Tenor<br>
          Kammersymphonie Ostfelde<br>
          Kirchenkreiskantorei Steinbrück<br>
          Kantorei St. Aegidien, Wellmar
          <div class="gap"></div>
          Gesamtleitung:<br>
          Kirchenkreiskantoren<br>
          Tobias Reinhold (STB)<br>
          Simon Achterberg (WM)
        </div>
        <div class="facts">
          Sonntag, 13.10.2024<br>
          Beginn: 19.00 Uhr<br>
          Einlass: 18.30 Uhr<br>
          Stadthalle Wellmar<br>
          Eintrittspreise: 28,- / 22,- / 12,- EUR<br>
          (Ermäßigungen 40%)
          <div class="gap"></div>
          Kartenvorverkauf:<br>
          Kulturverein Wellmar<br>
          Lindengasse 7, 29411 WM
        </div>
      </div>
      <div class="more">
        Weitere Informationen<br>
        <span class="links"><span>aegidien-wellmar.de</span><span>kulturverein-wellmar.de</span><span>stadthalle-wellmar.de</span></span>
      </div>
    </section>

    <div class="brand-tower"><span class="dot"></span>Kantorei St. Aegidien</div>
    <div class="sponsors">
      <span class="sponsor">Kirchenkreis Wellmar</span>
      <span class="sponsor">Landkreis Wellmar Stiftung</span>
    </div>
  </main>
</body>
</html>
```